Event branding Sales presentation PowerPoint template required

We are looking to freshen up & step up the professional quality of our powerpoint presentation template. I am looking for a professional designer with good creative background to design a new template for our presentations to new clients and for bespoke projects.
We have attached our current PPP as well as an elevator pitch which has most of the information we would like on the template

We have 3 main parts of our business which are:
- Event Branding
- Fan Engagements
- Set builds / Theming

Target Market(s)

Event organisers and sporting fedrations

Industry/Entity Type

Events

Requirements
Must have
• Ability for easy editing. Strong visual representation
Nice to have
• Information pages as well as look-book pages
Should not have
• Overcrowded graphics / arty graphics

```html
<!DOCTYPE html>
<html lang="en">
<head>
<meta charset="utf-8">
<title>Vantage Events – Presentation Template Overview</title>
<link href="https://fonts.googleapis.com/css2?family=Poppins:ital,wght@0,300;0,400;0,500;0,600;0,700;1,400&display=swap" rel="stylesheet">
<style>
:root{
  --gold:#c98b2b;
  --gold-light:#e2b160;
  --ink:#0e0e0e;
  --paper:#ffffff;
  --mist:#ececec;
  --board:#cfcfd1;
  --text:#2b2b2b;
  --muted:#777;
}
*{margin:0;padding:0;box-sizing:border-box}
html,body{width:1200px;height:781px;overflow:hidden;background:var(--board);font-family:'Poppins',sans-serif;color:var(--text)}
.board{position:relative;width:1200px;height:781px}
.slide{position:absolute;width:370px;height:208px;transform:scale(.5043);transform-origin:0 0;overflow:hidden;background:var(--paper);box-shadow:0 3px 8px rgba(0,0,0,.25)}
.slide.light::after{content:"";position:absolute;left:0;right:0;bottom:0;height:3px;background:var(--gold)}
.slide.dark{background:var(--ink);color:#fff}
.slide.gold{background:var(--gold);color:#fff}
.abs{position:absolute}
.title{position:absolute;left:0;right:0;top:14px;text-align:center;font-weight:600;font-size:10px;color:var(--gold)}
.title::before{content:"";display:block;width:14px;height:1px;background:var(--gold);margin:0 auto 3px}
.title.caps{text-transform:uppercase;font-weight:700}
.sub{position:absolute;left:0;right:0;text-align:center;font-size:4px;color:var(--text)}
.tiny{font-size:3.4px;line-height:1.45;color:var(--muted)}
.small-logo{position:absolute;left:14px;bottom:7px;display:flex;align-items:center;gap:2px;font-size:3px;color:var(--gold);font-weight:500}
.small-logo i{width:6px;height:6px;border:0.6px solid var(--gold);border-radius:50%}
.photo{position:absolute}
.gold-h{color:var(--gold);font-weight:600}
.circle-photo{position:absolute;border-radius:50%;border:2px solid #fff;background:linear-gradient(160deg,#d7c3ad,#7d6652)}
.toc-item{position:absolute;width:86px;display:flex;justify-content:space-between;font-size:4.6px;border-bottom:0.6px solid var(--gold);padding-bottom:2px}
.toc-item b{font-weight:600}
.stat{position:absolute;text-align:center;font-size:4.6px}
.stat b{display:block;color:var(--gold);font-size:6px;font-weight:600}
.card{position:absolute;border-radius:6px;text-align:center;color:#fff;padding:8px 6px}
.card h4{font-size:5px;font-weight:600;margin:4px 0 2px}
.card p{font-size:3.4px;line-height:1.45}
table{border-collapse:collapse;font-size:4px;color:#fff;width:100%}
th{background:var(--ink);text-align:left;font-weight:600;padding:3px 3px}
td{padding:2px 3px;vertical-align:top}
tr.band td{background:var(--ink)}
.point{position:absolute;width:36px;height:36px;border-radius:50%;background:var(--gold);border:2px solid #fff;text-align:center;padding-top:8px;font-size:8px;font-weight:700;line-height:1}
.point span{font-size:3.2px;font-weight:400}
</style>
</head>
<body>
<main class="board">

<!-- 1 Cover -->
<section class="slide dark" style="left:57.5px;top:59.5px">
  <div class="abs" style="left:0;right:0;top:28px;display:flex;flex-direction:column;align-items:center;gap:4px">
    <span style="width:22px;height:22px;border:1px solid var(--gold);border-radius:50%"></span>
    <span style="font-size:5.5px;letter-spacing:1.6px;color:var(--gold)">VANTAGE EVENTS</span>
  </div>
  <div class="abs" style="left:0;right:0;top:92px;text-align:center;font-weight:300;font-size:12px">PRESENTATION TITLE</div>
  <div class="abs" style="left:0;right:0;top:112px;text-align:center;font-weight:600;font-size:8px">SUBTITLE</div>
  <div class="abs" style="left:16px;bottom:8px;font-size:4.5px">JANUARY 2023</div>
  <div class="abs" style="right:16px;bottom:8px;font-size:4.5px">WWW.VANTAGE-EVENTS.CO</div>
</section>

<!-- 2 Contents -->
<section class="slide light" style="left:281.9px;top:59.5px">
  <h2 class="title">Contents</h2>
  <div class="toc-item" style="left:55px;top:50px"><span>Cover Slide</span><b>01</b></div>
  <div class="toc-item" style="left:55px;top:75px"><span>Contents</span><b>03</b></div>
  <div class="toc-item" style="left:55px;top:102px"><span>About Us</span><b>04</b></div>
  <div class="toc-item" style="left:55px;top:130px"><span>Our Mission</span><b>06</b></div>
  <div class="toc-item" style="left:55px;top:160px"><span>Our Vission</span><b>07</b></div>
  <div class="toc-item" style="left:208px;top:50px"><span>Infographic 1</span><b>01</b></div>
  <div class="toc-item" style="left:208px;top:75px"><span>Planning</span><b>03</b></div>
  <div class="toc-item" style="left:208px;top:102px"><span>Company info</span><b>04</b></div>
  <div class="toc-item" style="left:208px;top:130px"><span>Our Team</span><b>06</b></div>
  <div class="toc-item" style="left:208px;top:160px"><span>Dashboard</span><b>07</b></div>
  <div class="small-logo"><i></i>VANTAGE</div>
</section>

<!-- 3 Vision -->
<section class="slide light" style="left:518.3px;top:59.5px">
  <h2 class="title">Our Vision</h2>
  <div class="abs" style="left:18px;right:0;top:56px;height:66px;background:var(--gold);color:#fff;font-style:italic;font-size:6.3px;line-height:1.75;padding:5px 18px">Lorem ipsum dolor sit amet, consectetuer adipiscing elit, sed diam nonummy nibh euismod tincidunt ut laoreet dolore magna aliquam erat volutpat. Ut wisi enim ad minim veniam, quis nostrud exerci tation ullamcorper suscipit lobortis nisl ut aliquip ex ea commodo consequat. Duis</div>
  <div class="small-logo"><i></i>VANTAGE</div>
</section>

<!-- 4 Mission -->
<section class="slide light" style="left:757.8px;top:59.5px">
  <div class="abs" style="left:255px;top:0;width:115px;height:208px;background:var(--ink)"></div>
  <h2 class="title">Our Mission</h2>
  <div class="abs" style="left:25px;top:56px;width:56px;height:44px;background:var(--mist);box-shadow:0 2px 4px rgba(0,0,0,.2)"></div>
  <div class="abs tiny" style="left:28px;top:62px;width:50px;text-align:center"><b class="gold-h" style="font-size:4.5px;display:block">Mission 1</b>Our plan for bold and lasting event brands.</div>
  <div class="abs tiny" style="left:132px;top:62px;width:58px;text-align:center"><b class="gold-h" style="font-size:4.5px;display:block">Mission 1</b>Clear builds and signage made for each venue.</div>
  <div class="abs tiny" style="left:262px;top:62px;width:100px;text-align:center;color:#bbb"><b class="gold-h" style="font-size:4.5px;display:block">Mission 1</b>Fan moments that stay with crowds long after.</div>
  <div class="abs tiny" style="left:25px;top:115px;width:56px;text-align:center"><b class="gold-h" style="font-size:4.5px;display:block">Mission 1</b>Safe rigging and smooth install on every site.</div>
  <div class="abs tiny" style="left:132px;top:115px;width:58px;text-align:center"><b class="gold-h" style="font-size:4.5px;display:block">Mission 1</b>Print and theming made in one trusted place.</div>
  <div class="abs tiny" style="left:262px;top:115px;width:100px;text-align:center;color:#bbb"><b class="gold-h" style="font-size:4.5px;display:block">Mission 1</b>Partners who care about each small detail.</div>
  <div class="small-logo"><i></i>VANTAGE</div>
</section>

<!-- 5 About -->
<section class="slide light" style="left:987.3px;top:59.5px">
  <div class="photo" role="img" aria-label="Large colourful letter sculptures on a lawn at an outdoor event" style="left:0;top:0;width:142px;height:205px;background:linear-gradient(120deg,#86c24a 0%,#5aa33a 35%,#e4574e 55%,#c84848 75%,#6e8f3c 100%)"></div>
  <div class="abs" style="left:155px;top:52px;font-size:7px;font-weight:700;color:var(--gold)">ABOUT US</div>
  <div class="abs" style="left:155px;top:63px;width:200px;font-size:3.6px;line-height:1.45">Vantage Events has a strong global presence with trusted partners. We bring a wealth of know-how with venues and events across the globe, building temporary and permanent branding, themes, set builds and signage so your brand is in good hands.</div>
  <div class="abs" style="left:155px;top:110px;width:58px;height:24px;background:var(--mist);font-size:4.4px;padding:4px 6px"><b class="gold-h">15</b><br>Companies</div>
  <div class="abs" style="left:216px;top:110px;width:58px;height:24px;background:var(--mist);font-size:4.4px;padding:4px 6px"><b class="gold-h">1,000</b><br>Clients</div>
  <div class="abs" style="left:277px;top:110px;width:58px;height:24px;background:var(--gold);color:#fff;font-size:4.4px;padding:4px 6px"><b>46</b><br>Employees</div>
  <div class="abs" style="left:155px;top:145px;font-size:4.4px;font-weight:600;color:var(--gold)">Pushing the boundaries, delivering the highest quality.</div>
</section>

<!-- 6 Services -->
<section class="slide light" style="left:57.5px;top:200.7px">
  <h2 class="title caps">Our Services</h2>
  <div class="sub tiny" style="top:34px;color:var(--text)">Lorem ipsum dolor sit amet, consectetuer adipiscing elit,<br>sed diam nonummy nibh euismod tincidunt ut laoreet</div>
  <div class="photo" role="img" aria-label="Glowing hexagonal stage entrance" style="left:18px;top:55px;width:92px;height:76px;background:radial-gradient(circle at 50% 55%,#ff6a3a 0%,#7a1a4a 35%,#1b1b3a 75%)"></div>
  <div class="photo" role="img" aria-label="Crowd of fans behind a thank-you banner in a stadium" style="left:139px;top:55px;width:92px;height:76px;background:linear-gradient(180deg,#c73b32,#d9624a 45%,#3f7a3d)"></div>
  <div class="photo" role="img" aria-label="Custom built theming set in a warehouse" style="left:260px;top:55px;width:92px;height:76px;background:linear-gradient(135deg,#6f7d72,#a8aea0 50%,#3f4a44)"></div>
  <div class="abs tiny" style="left:15px;top:143px;width:98px;text-align:center;color:var(--text)"><b class="gold-h" style="font-size:4.4px;display:block">Branding</b>A full approach to branding, with clear and lasting design for every venue and every size of event.</div>
  <div class="abs tiny" style="left:136px;top:143px;width:98px;text-align:center;color:var(--text)"><b class="gold-h" style="font-size:4.4px;display:block">Fan Engagement</b>Fan zones that make the day. We plan, build and deliver the moments crowds remember.</div>
  <div class="abs tiny" style="left:257px;top:143px;width:98px;text-align:center;color:var(--text)"><b class="gold-h" style="font-size:4.4px;display:block">Bespoke Builds</b>We design and build anything, from large sets to small props that lift your event.</div>
  <div class="small-logo"><i></i>VANTAGE</div>
</section>

<!-- 7 Unique -->
<section class="slide light" style="left:281.9px;top:200.7px">
  <h2 class="title caps">Unique Perspective</h2>
  <div class="sub tiny" style="top:31px;color:var(--text)">Our core business</div>
  <div class="abs" style="left:178px;top:52px;width:14px;height:1px;background:var(--gold)"></div>
  <div class="abs" style="left:40px;right:40px;top:60px;text-align:center;font-size:3.9px;line-height:1.6">One of our strongest traits is that our team comes from many industries and built our service around creative delivery. With skills in film, rigging, outdoor advertising and set builds, we offer fresh additions to your branding and fan engagement. This could be a simple 3D image on a bridge or a giant immersive set. We build our props in-house and join with trusted global partners where needed.</div>
  <div class="stat" style="left:12px;top:143px;width:50px"><b>2100</b>Evaluations</div>
  <div class="stat" style="left:92px;top:143px;width:70px"><b>3100</b>Production profitably</div>
  <div class="abs" style="left:212px;top:137px;width:56px;height:26px;background:var(--gold);box-shadow:0 2px 4px rgba(0,0,0,.25)"></div>
  <div class="stat" style="left:212px;top:143px;width:56px;color:#fff"><b style="color:#fff">2100</b>Companies</div>
  <div class="stat" style="left:305px;top:143px;width:50px"><b>14</b>Certifications</div>
  <div class="small-logo"><i></i>VANTAGE</div>
</section>

<!-- 8 Analysis -->
<section class="slide light" style="left:518.3px;top:200.7px">
  <h2 class="title">Analysis Chart</h2>
  <div class="abs" style="left:193px;top:48px;width:177px;height:160px;background:var(--gold)"></div>
  <div class="abs" style="left:10px;top:57px;font-size:4.4px;font-weight:600;color:var(--gold)">Bar Chart</div>
  <svg class="abs" style="left:10px;top:70px" width="170" height="95" aria-label="Bar chart" role="img">
    <g font-size="3" fill="#777">
      <text x="0" y="12">Cat 1</text><text x="0" y="29">Cat 2</text><text x="0" y="46">Cat 3</text><text x="0" y="63">Cat 4</text>
    </g>
    <g stroke="#ddd" stroke-width=".4"><line x1="18" y1="0" x2="18" y2="75"/><line x1="55" y1="0" x2="55" y2="75"/><line x1="92" y1="0" x2="92" y2="75"/><line x1="129" y1="0" x2="129" y2="75"/><line x1="166" y1="0" x2="166" y2="75"/></g>
    <rect x="18" y="8" width="38" height="5" fill="#c98b2b"/><rect x="56" y="8" width="25" height="5" fill="#111"/><rect x="81" y="8" width="46" height="5" fill="#888"/>
    <rect x="18" y="25" width="30" height="5" fill="#c98b2b"/><rect x="48" y="25" width="18" height="5" fill="#111"/><rect x="66" y="25" width="32" height="5" fill="#888"/>
    <rect x="18" y="42" width="26" height="5" fill="#c98b2b"/><rect x="44" y="42" width="28" height="5" fill="#111"/><rect x="72" y="42" width="22" height="5" fill="#888"/>
    <rect x="18" y="59" width="34" height="5" fill="#c98b2b"/><rect x="52" y="59" width="16" height="5" fill="#111"/><rect x="68" y="59" width="24" height="5" fill="#888"/>
    <text x="60" y="84" font-size="3" fill="#777">Series 1 · Series 2 · Series 3</text>
  </svg>
  <div class="abs" style="left:200px;top:56px;width:162px;color:#fff;font-size:3.4px;line-height:1.45">
    <b style="font-size:4.4px;display:block">Analysis 1</b>Sales rose in each quarter as fan zones grew across new venues and federations.
    <b style="font-size:4.4px;display:block;margin-top:9px">Analysis 2</b>Set builds held steady while print and signage work added a strong share of new jobs.
    <b style="font-size:4.4px;display:block;margin-top:9px">Analysis 3</b>Repeat clients drove most growth, with bespoke theming the fastest rising service line.
  </div>
  <div class="small-logo"><i></i>VANTAGE</div>
</section>

<!-- 9 Process -->
<section class="slide light" style="left:757.8px;top:200.7px">
  <div class="photo" role="img" aria-label="Stadium crowd beneath a giant projected display" style="left:0;top:0;width:147px;height:172px;background:linear-gradient(180deg,#2d3f63 0%,#4a5e86 45%,#1d2c5c 60%,#9a2c2c 100%)"></div>
  <div class="abs" style="left:182px;top:50px;font-size:8px;font-weight:600;color:var(--gold)">Process</div>
  <div class="abs tiny" style="left:182px;top:63px;width:170px;color:var(--text)">Lorem ipsum dolor sit amet, consectetuer adipiscing elit, sed diam nonummy nibh euismod tincidunt ut laoreet dolore magna</div>
  <svg class="abs" style="left:147px;top:80px" width="80" height="70" aria-hidden="true"><g stroke="#c98b2b" stroke-width=".7" fill="#c98b2b"><line x1="0" y1="10" x2="33" y2="10"/><path d="M33 8 L36 10 L33 12Z"/><line x1="0" y1="36" x2="48" y2="36"/><path d="M48 34 L51 36 L48 38Z"/><line x1="0" y1="62" x2="66" y2="62"/><path d="M66 60 L69 62 L66 64Z"/></g></svg>
  <div class="abs tiny" style="left:185px;top:85px;width:165px;color:var(--text)"><b class="gold-h" style="font-size:4.2px;display:block">Step 1</b>Brief, site visit and a clear plan for your event.</div>
  <div class="abs tiny" style="left:200px;top:111px;width:150px;color:var(--text)"><b class="gold-h" style="font-size:4.2px;display:block">Step 2</b>Design, sign-off and in-house production of all items.</div>
  <div class="abs tiny" style="left:218px;top:137px;width:135px;color:var(--text)"><b class="gold-h" style="font-size:4.2px;display:block">Step 3</b>Install, live support and a safe clean removal.</div>
  <div class="small-logo"><i></i>VANTAGE</div>
</section>

<!-- 10 Planning -->
<section class="slide light" style="left:987.3px;top:200.7px">
  <div class="abs" style="left:150px;top:0;width:220px;height:180px;background:var(--ink)"></div>
  <div class="photo" role="img" aria-label="Building wrap with large printed slogan and tree" style="left:18px;top:47px;width:152px;height:136px;background:linear-gradient(135deg,#8a8a90,#5d6068 55%,#6e8a4a)"></div>
  <div class="abs" style="left:185px;top:53px;font-size:8px;font-weight:600;color:#fff">Planning</div>
  <div class="abs" style="left:185px;top:66px;width:175px;font-size:3.5px;line-height:1.45;color:#ccc">We map every step early so your build runs on time and on budget.</div>
  <div class="abs" style="left:185px;top:88px;width:175px;font-size:3.4px;line-height:1.45;color:#bbb"><b style="color:#fff;font-size:4.2px;display:block">Lorem ipsum do</b>Site surveys, load plans and access checks done before any work begins on site.</div>
  <div class="abs" style="left:185px;top:122px;width:175px;font-size:3.4px;line-height:1.45;color:#bbb"><b style="color:#fff;font-size:4.2px;display:block">Lorem ipsum do</b>One project lead keeps your team informed from first sketch to final handover.</div>
  <div class="small-logo"><i></i>VANTAGE</div>
</section>

<!-- 11 Fan engagement -->
<section class="slide light" style="left:57.5px;top:330.3px">
  <div class="abs" style="left:0;top:0;width:370px;height:40px;background:var(--ink)"></div>
  <div class="abs" style="left:0;right:0;top:14px;text-align:center;font-size:8px;font-weight:700;color:var(--gold)">FAN ENGAGEMENT</div>
  <div class="abs" style="left:0;right:0;top:27px;text-align:center;font-size:3.6px;color:#fff">Builds | Print | Signage | Theming | Banners</div>
  <svg class="abs" style="left:0;top:40px" width="370" height="168" role="img" aria-label="Collage of event photos: letter sculptures, stadium pitch, fan banner, arena stage and city square">
    <polygon points="0,20 120,0 50,168 0,168" fill="#d4524a"/>
    <polygon points="0,90 30,168 0,168" fill="#6aa63f"/>
    <polygon points="122,0 252,0 252,45 104,45" fill="#2f6b3a"/>
    <polygon points="102,50 252,50 252,95 82,95" fill="#c23c34"/>
    <polygon points="80,100 252,100 252,168 52,168" fill="#b43a30"/>
    <rect x="256" y="0" width="114" height="65" fill="#4a5666"/>
    <rect x="256" y="69" width="114" height="48" fill="#8d97a0"/>
    <rect x="256" y="121" width="114" height="47" fill="#7c8f6a"/>
  </svg>
  <div class="abs" style="left:12px;bottom:6px;font-size:3.6px;color:#fff;font-weight:600">VANTAGE</div>
</section>

<!-- 12 Leaders -->
<section class="slide light" style="left:281.9px;top:330.3px">
  <h2 class="title">Our Leaders</h2>
  <div class="sub tiny" style="top:32px;color:var(--text)">Lorem ipsum dolor sit amet, consectetuer adipiscing elit,</div>
  <div class="abs" style="left:0;top:48px;width:370px;height:38px;background:var(--gold)"></div>
  <div class="circle-photo" role="img" aria-label="Portrait of a team leader" style="left:33px;top:62px;width:44px;height:44px"></div>
  <div class="circle-photo" role="img" aria-label="Portrait of a team leader" style="left:123px;top:62px;width:44px;height:44px"></div>
  <div class="circle-photo" role="img" aria-label="Portrait of a team leader" style="left:213px;top:62px;width:44px;height:44px"></div>
  <div class="circle-photo" role="img" aria-label="Portrait of a team leader" style="left:295px;top:62px;width:44px;height:44px"></div>
  <div class="abs tiny" style="left:15px;top:111px;width:80px;text-align:center;color:var(--text)"><b class="gold-h" style="font-size:4px;display:block">Daniel Reed</b>Manager<br>Leads our brand team and client plans for each event.</div>
  <div class="abs tiny" style="left:105px;top:111px;width:80px;text-align:center;color:var(--text)"><b class="gold-h" style="font-size:4px;display:block">Daniel Reed</b>Manager<br>Runs fan zones and live crowd work at every venue.</div>
  <div class="abs tiny" style="left:195px;top:111px;width:80px;text-align:center;color:var(--text)"><b class="gold-h" style="font-size:4px;display:block">Daniel Reed</b>Manager<br>Heads set builds, rigging and safe site install work.</div>
  <div class="abs tiny" style="left:277px;top:111px;width:80px;text-align:center;color:var(--text)"><b class="gold-h" style="font-size:4px;display:block">Daniel Reed</b>Manager<br>Oversees print, signage and all theming production.</div>
  <div class="small-logo"><i></i>VANTAGE</div>
</section>

<!-- 13 Team -->
<section class="slide dark" style="left:518.3px;top:330.3px">
  <h2 class="title">Our Team</h2>
  <div class="abs" style="left:295px;top:40px;width:80px;height:80px;background:var(--gold);border-radius:8px 0 0 8px"></div>
  <div class="circle-photo" role="img" aria-label="Team member portrait" style="left:41px;top:52px;width:44px;height:44px"></div>
  <div class="circle-photo" role="img" aria-label="Team member portrait" style="left:131px;top:52px;width:44px;height:44px"></div>
  <div class="circle-photo" role="img" aria-label="Team member portrait" style="left:223px;top:52px;width:44px;height:44px"></div>
  <div class="circle-photo" role="img" aria-label="Team member portrait" style="left:306px;top:52px;width:44px;height:44px"></div>
  <div class="circle-photo" role="img" aria-label="Team member portrait" style="left:41px;top:128px;width:44px;height:44px"></div>
  <div class="circle-photo" role="img" aria-label="Team member portrait" style="left:131px;top:128px;width:44px;height:44px"></div>
  <div class="circle-photo" role="img" aria-label="Team member portrait" style="left:223px;top:128px;width:44px;height:44px"></div>
  <div class="circle-photo" role="img" aria-label="Team member portrait" style="left:306px;top:128px;width:44px;height:44px"></div>
  <div class="abs" style="left:33px;top:99px;width:60px;text-align:center;font-size:3.6px"><b style="color:var(--gold)">Daniel Reed</b><br><span style="color:#aaa">Manager</span></div>
  <div class="abs" style="left:123px;top:99px;width:60px;text-align:center;font-size:3.6px"><b style="color:var(--gold)">Daniel Reed</b><br><span style="color:#aaa">Manager</span></div>
  <div class="abs" style="left:215px;top:99px;width:60px;text-align:center;font-size:3.6px"><b style="color:var(--gold)">Daniel Reed</b><br><span style="color:#aaa">Manager</span></div>
  <div class="abs" style="left:298px;top:99px;width:60px;text-align:center;font-size:3.6px"><b>Daniel Reed</b><br>Manager</div>
  <div class="abs" style="left:33px;top:175px;width:60px;text-align:center;font-size:3.6px"><b style="color:var(--gold)">Daniel Reed</b><br><span style="color:#aaa">Manager</span></div>
  <div class="abs" style="left:123px;top:175px;width:60px;text-align:center;font-size:3.6px"><b style="color:var(--gold)">Daniel Reed</b><br><span style="color:#aaa">Manager</span></div>
  <div class="abs" style="left:215px;top:175px;width:60px;text-align:center;font-size:3.6px"><b style="color:var(--gold)">Daniel Reed</b><br><span style="color:#aaa">Manager</span></div>
  <div class="abs" style="left:298px;top:175px;width:60px;text-align:center;font-size:3.6px"><b style="color:var(--gold)">Daniel Reed</b><br><span style="color:#aaa">Manager</span></div>
  <div class="abs" style="left:0;right:0;bottom:0;height:3px;background:var(--gold)"></div>
</section>

<!-- 14 Turnkey -->
<section class="slide light" style="left:757.8px;top:330.3px">
  <h2 class="title caps">Turnkey Solutions</h2>
  <svg class="abs" style="left:0;top:55px" width="370" height="90" aria-hidden="true">
    <defs><path id="hex" d="M0 -17 L15 -8.5 L15 8.5 L0 17 L-15 8.5 L-15 -8.5Z"/></defs>
    <g><use href="#hex" x="35" y="33" fill="#111"/><use href="#hex" x="87" y="20" fill="#c98b2b"/><use href="#hex" x="138" y="33" fill="#111"/><use href="#hex" x="190" y="20" fill="#c98b2b"/><use href="#hex" x="241" y="33" fill="#111"/><use href="#hex" x="292" y="20" fill="#c98b2b"/><use href="#hex" x="343" y="33" fill="#111"/></g>
    <g fill="none" stroke="#fff" stroke-width="1">
      <circle cx="35" cy="33" r="5"/><path d="M31 37 L39 29"/>
      <rect x="82" y="14" width="10" height="12" rx="1"/><path d="M84 18 H90 M84 21 H90"/>
      <circle cx="138" cy="31" r="4"/><path d="M136 37 H140 M138 24 V22 M131 31 H129 M145 31 H147"/>
      <path d="M186 26 V16 L190 14 L194 16 V26Z"/>
      <path d="M241 40 C236 33 236 27 241 26 C246 27 246 33 241 40Z"/><circle cx="241" cy="30" r="1.5"/>
      <circle cx="292" cy="20" r="4"/><circle cx="292" cy="20" r="7" stroke-dasharray="2 2"/>
      <path d="M336 34 L340 30 L344 33 L350 28 M336 36 H350"/>
    </g>
    <g font-size="3.6" fill="#c98b2b" font-weight="600" text-anchor="middle" font-family="Poppins, sans-serif">
      <text x="35" y="62">Concept</text><text x="87" y="48">Srvey &amp; proposal</text><text x="138" y="62">Design</text><text x="190" y="48">Build / Print</text><text x="241" y="62">International</text><text x="241" y="67">Logistics</text><text x="292" y="48">Installing</text><text x="292" y="53">&amp; Rigging</text><text x="343" y="62">Full Project</text><text x="343" y="67">Management</text>
    </g>
  </svg>
  <div class="abs" style="left:0;top:148px;width:370px;height:28px;background:var(--ink)"></div>
  <div class="abs" style="left:18px;top:152px;width:250px;font-size:3.9px;font-weight:600;color:#fff;line-height:1.4">Vantage Events can assist through every step of your event. Providing the highest standards of delivery, our professionals will guide you through each technical milestone. Reaching your goals, together.</div>
  <div class="small-logo"><i></i>VANTAGE</div>
</section>

<!-- 15 Infographic -->
<section class="slide dark" style="left:987.3px;top:330.3px">
  <div class="abs" style="left:0;right:0;top:16px;text-align:center;font-size:8px;font-weight:600">infographic 03</div>
  <div class="abs" style="left:178px;top:28px;width:14px;height:1px;background:var(--gold)"></div>
  <div class="card" style="left:20px;top:70px;width:68px;height:100px;background:var(--gold);border-radius:0 0 14px 0;text-align:left;padding:40px 8px 0"><h4>Step One</h4><p>Short notes on the first step of your event plan.</p></div>
  <div class="card" style="left:107px;top:70px;width:68px;height:100px;background:var(--gold);border-radius:0 0 14px 0;text-align:left;padding:40px 8px 0"><h4>Step Two</h4><p>Short notes on the second step of your event plan.</p></div>
  <div class="card" style="left:195px;top:70px;width:68px;height:100px;background:var(--gold);border-radius:0 0 14px 0;text-align:left;padding:40px 8px 0"><h4>Step Three</h4><p>Short notes on the third step of your event plan.</p></div>
  <div class="card" style="left:283px;top:70px;width:68px;height:100px;background:var(--gold);border-radius:0 0 14px 0;text-align:left;padding:40px 8px 0"><h4>Step Four</h4><p>Short notes on the fourth step of your event plan.</p></div>
  <div class="point" style="left:34px;top:60px">500<br><span>Point A</span></div>
  <div class="point" style="left:121px;top:60px">600<br><span>Point B</span></div>
  <div class="point" style="left:209px;top:60px">700<br><span>Point C</span></div>
  <div class="point" style="left:297px;top:60px">800<br><span>Point D</span></div>
  <div class="abs" style="left:14px;bottom:6px;font-size:3.6px;font-weight:600">VANTAGE</div>
</section>

<!-- 16 Why -->
<section class="slide light" style="left:57.5px;top:459.8px">
  <h2 class="title" style="font-weight:700">WHY Vantage Events?</h2>
  <div class="card" style="left:37px;top:57px;width:90px;height:106px;background:var(--gold);box-shadow:0 2px 5px rgba(0,0,0,.25)">
    <svg width="14" height="14" aria-hidden="true"><circle cx="7" cy="6" r="3.5" fill="none" stroke="#fff" stroke-width=".8"/><path d="M5 11 H9 M7 0.5 V1.5 M1 6 H2 M12 6 H13" stroke="#fff" stroke-width=".8"/></svg>
    <h4>Knowledge</h4><p>With our own methods, years of skill and modern kit, you can trust that each event project is handled safely and smoothly. The word impossible is not in our vocabulary.</p></div>
  <div class="card" style="left:142px;top:57px;width:90px;height:106px;background:var(--ink);box-shadow:0 2px 5px rgba(0,0,0,.25)">
    <svg width="14" height="14" aria-hidden="true"><rect x="1.5" y="2" width="11" height="8" rx="1.5" fill="none" stroke="#fff" stroke-width=".8"/><path d="M4 10 L4 13 L7 10" fill="none" stroke="#fff" stroke-width=".8"/></svg>
    <h4>Experience</h4><p>We take on complex projects with rigging, custom built structures and tough access sites. Our team are fully trained and certified, with clear project control and fabrication.</p></div>
  <div class="card" style="left:247px;top:57px;width:90px;height:106px;background:var(--gold);box-shadow:0 2px 5px rgba(0,0,0,.25)">
    <svg width="16" height="14" aria-hidden="true"><circle cx="5" cy="4" r="2" fill="#fff"/><circle cx="11" cy="4" r="2" fill="#fff"/><path d="M1 12 C1 7 9 7 9 12Z M7 12 C7 7 15 7 15 12Z" fill="#fff"/></svg>
    <h4>Results</h4><p>We offer a bespoke service for each and every client, with skill in design and install second to none. We turn your ideas into an amazing result. Your success is our success.</p></div>
  <div class="small-logo"><i></i>VANTAGE</div>
</section>

<!-- 17 Table -->
<section class="slide gold" style="left:281.9px;top:459.8px">
  <div class="abs" style="left:0;right:0;top:16px;text-align:center;font-size:9px;font-weight:600">Table</div>
  <div class="abs" style="left:0;right:0;top:29px;text-align:center;font-size:3.6px">Lorem ipsum dolor sit amet, consectetuer adipiscing elit,</div>
  <div class="abs" style="left:52px;top:52px;width:266px">
    <table>
      <tr><th>Data Name</th><th>Product</th><th>Profit</th><th>Optional</th><th>Sold</th><th>Performance</th></tr>
      <tr><td>Data 1</td><td>Product<br>Name</td><td>$000,000.00</td><td>Yes</td><td>70</td><td>45%</td></tr>
      <tr class="band"><td>Data 2</td><td>Product<br>Name</td><td>$000,000.00</td><td>No</td><td>30</td><td>20%</td></tr>
      <tr><td>Data 3</td><td>Product<br>Name</td><td>$000,000.00</td><td>No</td><td>20</td><td>15%</td></tr>
      <tr class="band"><td>Data 4</td><td>Product<br>Name</td><td>$000,000.00</td><td>Yes</td><td>100</td><td>60%</td></tr>
      <tr><td>Data 5</td><td>Product<br>Name</td><td>$000,000.00</td><td>Yes</td><td>50</td><td>40%</td></tr>
    </table>
  </div>
  <div class="abs" style="left:14px;bottom:6px;font-size:3.6px;font-weight:600">VANTAGE</div>
</section>

<!-- 18 Dashboard 01 -->
<section class="slide light" style="left:518.3px;top:459.8px">
  <h2 class="title">Dashboard 01</h2>
  <div class="stat" style="left:5px;top:56px;width:65px;color:var(--text)">Customers<b>2100</b></div>
  <div class="stat" style="left:90px;top:56px;width:65px;color:var(--text)">Profitably<b>3100</b></div>
  <div class="abs" style="left:210px;top:48px;width:54px;height:24px;background:var(--gold);box-shadow:0 2px 4px rgba(0,0,0,.25)"></div>
  <div class="stat" style="left:210px;top:52px;width:54px;color:#fff">Projects<b style="color:#fff">300</b></div>
  <div class="stat" style="left:300px;top:56px;width:55px;color:var(--text)">Returns<b>14</b></div>
  <div class="abs tiny" style="left:10px;top:90px;color:var(--text)"><b class="gold-h">5 Active Users</b><br>&nbsp;&nbsp;Last 10 Days</div>
  <div class="abs tiny" style="left:95px;top:90px;color:var(--text)"><b class="gold-h">2 Users per role</b><br>&nbsp;&nbsp;Last 10 Days</div>
  <svg class="abs" style="left:12px;top:122px" width="100" height="55" role="img" aria-label="Stacked bar chart">
    <g stroke="#ddd" stroke-width=".4"><line x1="14" y1="0" x2="14" y2="45"/><line x1="90" y1="0" x2="90" y2="45"/></g>
    <rect x="14" y="3" width="20" height="4" fill="#c98b2b"/><rect x="34" y="3" width="15" height="4" fill="#111"/><rect x="49" y="3" width="26" height="4" fill="#888"/>
    <rect x="14" y="13" width="16" height="4" fill="#c98b2b"/><rect x="30" y="13" width="12" height="4" fill="#111"/><rect x="42" y="13" width="18" height="4" fill="#888"/>
    <rect x="14" y="23" width="14" height="4" fill="#c98b2b"/><rect x="28" y="23" width="16" height="4" fill="#111"/><rect x="44" y="23" width="12" height="4" fill="#888"/>
    <rect x="14" y="33" width="18" height="4" fill="#c98b2b"/><rect x="32" y="33" width="10" height="4" fill="#111"/><rect x="42" y="33" width="14" height="4" fill="#888"/>
  </svg>
  <svg class="abs" style="left:150px;top:120px" width="60" height="60" role="img" aria-label="Donut chart">
    <circle cx="30" cy="28" r="20" fill="none" stroke="#c98b2b" stroke-width="5" stroke-dasharray="90 126" transform="rotate(-90 30 28)"/>
    <circle cx="30" cy="28" r="20" fill="none" stroke="#111" stroke-width="5" stroke-dasharray="26 126" stroke-dashoffset="-90" transform="rotate(-90 30 28)"/>
    <circle cx="30" cy="28" r="20" fill="none" stroke="#bbb" stroke-width="5" stroke-dasharray="10 126" stroke-dashoffset="-116" transform="rotate(-90 30 28)"/>
  </svg>
  <div class="abs" style="left:253px;top:125px;font-size:4px;color:var(--gold);line-height:1.7"><b>Live Profit &amp; Net Sales</b><br>Net Profit<br><b>$55.432M</b><br>Sales ~ 400,000</div>
  <div class="small-logo"><i></i>VANTAGE</div>
</section>

<!-- 19 Dashboard 02 -->
<section class="slide light" style="left:757.8px;top:459.8px">
  <h2 class="title">Dashboard 02</h2>
  <svg class="abs" style="left:12px;top:50px" width="360" height="150" role="img" aria-label="Column chart, pie chart and four area charts">
    <text x="5" y="5" font-size="3" fill="#c98b2b" font-family="Poppins, sans-serif">Chart Title</text>
    <line x1="16" y1="8" x2="16" y2="62" stroke="#ddd" stroke-width=".4"/>
    <line x1="16" y1="62" x2="170" y2="62" stroke="#ddd" stroke-width=".4"/>
    <g fill="#c98b2b"><rect x="22" y="14" width="6" height="48"/><rect x="37" y="14" width="6" height="48"/><rect x="52" y="14" width="6" height="48"/><rect x="67" y="14" width="6" height="48"/><rect x="82" y="14" width="6" height="48"/><rect x="97" y="14" width="6" height="48"/><rect x="112" y="14" width="6" height="48"/><rect x="127" y="14" width="6" height="48"/><rect x="142" y="14" width="6" height="48"/><rect x="157" y="14" width="6" height="48"/></g>
    <g transform="translate(290 35)">
      <path d="M0 0 L0 -20 A20 20 0 1 1 -12 16Z" fill="#c98b2b"/>
      <path d="M0 0 L-12 16 A20 20 0 0 1 -19 -6Z" fill="#111"/>
      <path d="M0 0 L-19 -6 A20 20 0 0 1 -8 -18Z" fill="#999"/>
      <path d="M0 0 L-8 -18 A20 20 0 0 1 0 -20Z" fill="#ccc"/>
    </g>
    <g transform="translate(8 90)"><path d="M0 35 L0 15 C15 5 30 8 55 0 L55 35Z" fill="#c98b2b"/><path d="M0 35 L20 25 L40 15 L55 8 L55 35Z" fill="#111"/></g>
    <g transform="translate(92 90)"><path d="M0 35 L0 15 C15 5 30 8 55 0 L55 35Z" fill="#c98b2b"/><path d="M0 35 L20 25 L40 15 L55 8 L55 35Z" fill="#111"/></g>
    <g transform="translate(182 90)"><path d="M0 35 L0 15 C15 5 30 8 55 0 L55 35Z" fill="#c98b2b"/><path d="M0 35 L20 25 L40 15 L55 8 L55 35Z" fill="#111"/></g>
    <g transform="translate(268 90)"><path d="M0 35 L0 15 C15 5 30 8 55 0 L55 35Z" fill="#c98b2b"/><path d="M0 35 L20 25 L40 15 L55 8 L55 35Z" fill="#111"/></g>
  </svg>
  <div class="small-logo"><i></i>VANTAGE</div>
</section>

<!-- 20 Thank you -->
<section class="slide gold" style="left:987.3px;top:459.8px">
  <div class="abs" style="left:0;right:0;top:55px;text-align:center;font-size:18px;font-weight:300">THANK YOU</div>
  <div class="abs" style="left:50px;right:50px;top:88px;text-align:center;font-size:3.9px;line-height:1.5">Lorem ipsum dolor sit amet, consectetuer adipiscing elit, sed diam nonummy nibh euismod tincidunt ut laoreet dolore magna aliquam erat volutpat. Ut wisi enim ad minim veniam, quis nostrud exerci tation ullamcorper suscipit lobortis nisl ut aliquip</div>
</section>

<!-- 21 Icon set -->
<section class="slide dark" style="left:57.5px;top:601.5px">
  <svg class="abs" style="left:0;top:0" width="370" height="208" aria-label="Set of gold line icons" role="img">
    <g fill="none" stroke="#c98b2b" stroke-width="1.1" stroke-linecap="round" stroke-linejoin="round">
      <g transform="translate(45 30)"><circle r="5"/><path d="M-8 0H-5M5 0H8M0 -8V-5M0 5V8"/></g>
      <g transform="translate(112 30)"><rect x="-5" y="-7" width="10" height="14" rx="1"/><path d="M-3 -3H3M-3 0H3M-3 3H1"/></g>
      <g transform="translate(184 30)"><circle r="7"/><path d="M-7 0H7M0 -7C-4 -3 -4 3 0 7M0 -7C4 -3 4 3 0 7"/></g>
      <g transform="translate(255 30)"><circle r="4"/><circle r="7" stroke-dasharray="2 2"/></g>
      <g transform="translate(321 30)"><path d="M-7 -2H7V6H-7Z M-5 -2L-2 -6H2L5 -2"/></g>
      <g transform="translate(45 67)"><circle r="6"/><path d="M0 -3V0L2 2"/></g>
      <g transform="translate(112 67)"><circle cx="-2" r="4"/><path d="M1 3L6 7"/></g>
      <g transform="translate(184 67)"><rect x="-6" y="-5" width="12" height="8" rx="1.5"/><path d="M-3 3V6L0 3"/></g>
      <g transform="translate(255 67)"><circle cy="-1" r="4"/><path d="M-2 5H2M0 -8V-7M-7 -1H-6M6 -1H7"/></g>
      <g transform="translate(321 67)"><path d="M-6 -2V2H-3L4 6V-6L-3 -2Z"/></g>
      <g transform="translate(45 100)"><circle r="5"/><path d="M-4 4L4 -4"/></g>
      <g transform="translate(112 100)"><circle cy="-1" r="4"/><path d="M-2 5H2"/></g>
      <g transform="translate(184 100)"><circle cx="-4" cy="-3" r="2" fill="#c98b2b"/><circle cx="4" cy="-3" r="2" fill="#c98b2b"/><path d="M-8 5C-8 0 0 0 0 5ZM0 5C0 0 8 0 8 5Z" fill="#c98b2b"/></g>
      <g transform="translate(255 100)"><path d="M-5 -6C-7 -2 -2 6 5 6L6 3L3 1L1 3C-1 2 -3 0 -3 -2L-1 -3L-3 -7Z"/></g>
      <g transform="translate(321 100)"><path d="M-7 0L-3 -3L0 -1L3 -3L7 0L3 4L0 2L-3 4Z"/></g>
      <g transform="translate(45 133)"><path d="M-6 5H6M-5 5V2M-2 5V-1M1 5V-3M4 5V-5"/></g>
      <g transform="translate(112 133)"><rect x="-5" y="-7" width="10" height="14" rx="1"/><path d="M-2 1L0 3L3 -2"/></g>
      <g transform="translate(184 133)"><path d="M0 -7L6 -4V1C6 4 3 6 0 7C-3 6 -6 4 -6 1V-4Z"/></g>
      <g transform="translate(255 133)"><circle r="3" fill="#c98b2b"/><circle cx="-5" cy="-3" r="2" fill="#c98b2b"/><circle cx="5" cy="-3" r="2" fill="#c98b2b"/></g>
      <g transform="translate(321 133)"><circle r="3"/><circle r="6" stroke-dasharray="3 2"/></g>
      <g transform="translate(45 166)"><path d="M-4 6V-2L0 -6L4 -2V6Z"/></g>
      <g transform="translate(112 166)"><path d="M0 -6L6 -3V3L0 6L-6 3V-3Z M-6 -3L0 0L6 -3M0 0V6"/></g>
      <g transform="translate(184 166)"><path d="M0 7C-5 1 -5 -3 0 -6C5 -3 5 1 0 7Z"/><circle cy="-2" r="1.6"/></g>
      <g transform="translate(255 166)"><rect x="-7" y="-5" width="14" height="10" rx="1"/><path d="M-7 -5L0 1L7 -5"/></g>
      <g transform="translate(321 166)"><circle cy="-3" r="3"/><path d="M-6 6C-6 1 6 1 6 6Z"/></g>
    </g>
  </svg>
</section>

</main>
</body>
</html>
```